Luftpolster-Versandtaschen  designen
Luftpolster-Versandtaschen designen
Zielgruppe
Es ist eine natürliche Schmerzsalbe entwickelt und hergestellt in Deutschland.
Die PELOR Salbe gibt ein zuverlässige Gefühl, durch ein innovatives Naturprodukt erstaunlich schnelle, wirkungsvolle Hilfe bei Schmerzen des Bewegungsapparates und bei Hautschäden zu erhalten und dabei gleichzeitig die Haut zu pflegen.
Aufgabenstellung
Wir möchten unsere Luftpolster-Versandtaschen gestalten lassen und das Corporate Design dort platzieren.
Ziel soll sein, das der Kunde eine hohe Aufmerksamkeit schon, vor dem Öffnen und das Vertrauen erhöht, schnelle Wiedererkennung der Marke Pelor Naturbalsam.
Die Druckdateien benötigen wir als pdf oder jedwede andere Datei mit einer Mindestauflösung von 300 dpi. Die Farbdarstellung erfolgt in CMYK. Alle Grafiken werden mittig platziert und proportional angepasst. Die genauen Maße der Versandtaschen bitte den Dokument vorlage_packbag entnehmen.
Farben / Texte / Bilder können von den Dokument (neue_webseite_alle_seiten_uebersicht) verwendet werden.
Bitte die Datei (vorlage_packbag_14d.pdf) von der Druckerei beachten.

```html
<!DOCTYPE html>
<html lang="de">
<head>
<meta charset="utf-8">
<title>Pelor Naturbalsam – Versandtasche</title>
<link href="https://fonts.googleapis.com/css2?family=Open+Sans:ital,wght@0,600;0,700;0,800;1,600;1,700&display=swap" rel="stylesheet">
<style>
  :root {
    --backdrop: #eeeeee;
    --paper: #ffffff;
    --orange-deep: #ee7219;
    --orange-edge: #f3a35a;
    --orange-mid: #f8b845;
    --badge: #f4b662;
    --cream: #fff8ee;
    --grey-text: #8a8a8a;
    --grey-dark: #5f5f5f;
  }
  * { margin: 0; padding: 0; box-sizing: border-box; }
  html, body {
    width: 1200px; height: 877px; overflow: hidden;
    background: var(--backdrop);
    font-family: "Open Sans", sans-serif;
  }
  .mailer {
    position: absolute; left: 383px; top: 148px;
    width: 433px; height: 581px;
    background: var(--paper);
  }
  .brand {
    position: absolute; left: 0; right: 0; top: 76px;
    display: flex; align-items: center; justify-content: center; gap: 8px;
  }
  .brand-dot {
    width: 20px; height: 20px; border-radius: 50%;
    background: var(--orange-mid);
  }
  .brand-name {
    font-weight: 800; font-size: 19px; letter-spacing: 0.5px;
    color: var(--grey-dark);
  }
  .hero {
    position: absolute; left: 98px; top: 204px;
    width: 237px; height: 230px;
    background: linear-gradient(90deg, var(--orange-edge) 0%, var(--orange-mid) 30%, var(--orange-mid) 70%, var(--orange-edge) 100%);
  }
  .hero-text {
    position: absolute; left: 34px; top: 68px; width: 170px;
    line-height: 1;
  }
  .hero-title {
    color: var(--orange-deep); font-weight: 800; font-size: 33px;
    display: block; white-space: nowrap;
  }
  .hero-title.line-1 { letter-spacing: 3px; }
  .hero-title.line-2 { letter-spacing: 14px; margin-top: -3px; }
  .hero-claim {
    color: var(--cream); font-weight: 800; font-size: 20.5px;
    display: block; white-space: nowrap; line-height: 21px; margin-top: 4px;
  }
  .hero-claim + .hero-claim { margin-top: 0; }
  .tagline {
    position: absolute; left: 0; right: 0; top: 460px;
    text-align: center; font-style: italic; font-weight: 600;
    font-size: 11.6px; letter-spacing: 1px; color: var(--grey-text);
  }
  .benefits {
    position: absolute; left: 53px; top: 489px;
    display: flex; gap: 0;
  }
  .benefit {
    display: flex; align-items: center; gap: 3px; width: 118px;
  }
  .benefit-icon {
    width: 25px; height: 25px; border-radius: 50%;
    background: var(--badge); flex: none;
  }
  .benefit-label {
    font-style: italic; font-weight: 700; font-size: 5px;
    letter-spacing: 0.3px; color: var(--grey-text); white-space: nowrap;
  }
</style>
</head>
<body>
  <main class="mailer">
    <div class="brand">
      <span class="brand-dot"></span>
      <span class="brand-name">Pelor Naturbalsam</span>
    </div>

    <section class="hero">
      <div class="hero-text">
        <span class="hero-title line-1">ALWAYS</span>
        <span class="hero-title line-2">PELOR!</span>
        <span class="hero-claim">MIT DER KRAFT</span>
        <span class="hero-claim">AUS DER NATUR</span>
      </div>
    </section>

    <p class="tagline">Hält jung, macht beweglich.Mit der 10-Kräuter-Aktivformel</p>

    <ul class="benefits">
      <li class="benefit">
        <svg class="benefit-icon" viewBox="0 0 25 25" aria-hidden="true">
          <circle cx="12.5" cy="12.5" r="12.5" fill="var(--badge)"/>
          <path d="M12.5 5 C11 7.5 10.5 8.5 10.5 9.5 a2 2 0 0 0 4 0 c0-1-0.5-2-2-4.5z" fill="none" stroke="#fff" stroke-width="0.8"/>
          <path d="M5 17 l3-3 h6 a1 1 0 0 1 0 2 h-3 M14 16 l4-2.5 a1 1 0 0 1 1.2 1.6 L14 19 H7 l-2 1.5" fill="none" stroke="#fff" stroke-width="0.8" stroke-linecap="round" stroke-linejoin="round"/>
        </svg>
        <span class="benefit-label">ENTSPANNT UND REGENERIERT</span>
      </li>
      <li class="benefit">
        <svg class="benefit-icon" viewBox="0 0 25 25" aria-hidden="true">
          <circle cx="12.5" cy="12.5" r="12.5" fill="var(--badge)"/>
          <path d="M12.5 19 V12 M12.5 12 C11 8 7 8 6 9 c0 3 3 5 6.5 3z M12.5 12 c1.5-4 5.5-4 6.5-3 c0 3-3 5-6.5 3z" fill="none" stroke="#fff" stroke-width="0.8" stroke-linecap="round"/>
        </svg>
        <span class="benefit-label">100% NATUR</span>
      </li>
      <li class="benefit">
        <svg class="benefit-icon" viewBox="0 0 25 25" aria-hidden="true">
          <circle cx="12.5" cy="12.5" r="12.5" fill="var(--badge)"/>
          <path d="M5.5 12 h14 c0 3.5-3 6-7 6 s-7-2.5-7-6z M9.5 18.5 h6 M12.5 11 l2.5-5" fill="none" stroke="#fff" stroke-width="0.8" stroke-linecap="round" stroke-linejoin="round"/>
        </svg>
        <span class="benefit-label">STÄRKT, PFLEGT, SCHÜTZT</span>
      </li>
    </ul>
  </main>
</body>
</html>
```